依頼詳細
こちらでワイヤーフレームを作成していますので、ある程度それを参考にして頂きながら製作進めて頂けると思います。

また、下記のサイトをデザインの参考に制作をお願い致します。
https://hiseraku.jp/
https://www.sabeki.or.jp/
http://www.mirusa.or.jp/

イメージは
●シンプル
●対象は女性ですが「可愛らしく」よりは「大人っぽく」

以上、よろしくお願いします。
サイトURL
ページ数
2ページ
希望イメージ
シンプル 複雑
単色 カラフル
暗い 明るい
日常 高級
遊び心 厳粛
未来的 伝統的
女性的 男性的
希望する色
納品ファイル
• 高解像度JPG (.jpg)
• イラストレーター形式 (.ai)
• フォトショップ形式 (.psd)
• PNG形式 (.png)
補足説明
提案の締め切りを【2018年7月29日】に延長致します。
何卒宜しくお願い致します。
■ 選んだ理由

病院のイメージ通り、清潔感・信頼感・好感度が感じられるデザインで大変気に入りました。有難うございました。

■ 提案者全員のお礼・コメント

この度はデザイン案をいろいろと考え、ご提案していただき、有難うございました。またご縁がありましたら、何卒よろしくお願いします。

```html
<!DOCTYPE html>
<html lang="ja">
<head>
<meta charset="utf-8">
<title>空音産婦人科</title>
<link href="https://fonts.googleapis.com/css2?family=Noto+Sans+JP:wght@400;500;700&family=Noto+Serif+JP:wght@500;700&family=Montserrat:wght@400;500&display=swap" rel="stylesheet">
<style>
:root{
  --green:#7fc6ae;
  --green-dark:#5aae93;
  --pink:#ef7fa0;
  --text:#444;
  --line:#d9d9d9;
  --white:#fff;
}
*{box-sizing:border-box;margin:0;padding:0}
html,body{width:1200px;height:3184px;overflow:hidden}
body{font-family:"Noto Sans JP",sans-serif;color:var(--text);background:var(--white);position:relative;font-size:14px}
.abs{position:absolute}
.brand{font-family:"Montserrat",sans-serif;font-weight:500;letter-spacing:.08em;color:var(--green-dark);display:flex;align-items:center;gap:8px;white-space:nowrap}
.brand .dot{width:12px;height:12px;border-radius:50%;background:var(--green);flex:none}
/* header & hero */
.hero{left:0;top:0;width:1200px;height:860px;background:linear-gradient(160deg,#cfd8dc 0%,#eef2f1 40%,#d7e4e0 70%,#b9c8c4 100%)}
.header{left:0;top:0;width:1200px;height:60px;background:rgba(255,255,255,.88);display:flex;align-items:center;padding:0 40px;white-space:nowrap}
.header .brand{font-size:14px}
.nav{display:flex;gap:26px;margin-left:auto;font-size:12px;color:#555}
.tel{margin-left:30px;display:flex;align-items:center;gap:8px;font-family:"Montserrat",sans-serif;font-size:24px;color:#555;white-space:nowrap}
.tel-icon{width:30px;height:30px;border-radius:6px;background:#d23a3a;display:flex;align-items:center;justify-content:center;flex:none}
.reserve{left:1030px;top:140px;width:150px;height:40px;border-radius:20px;background:var(--pink);color:#fff;font-size:12px;display:flex;align-items:center;justify-content:center;white-space:nowrap}
.hero-copy{left:0;top:350px;width:1200px;text-align:center;color:#fff;text-shadow:0 1px 6px rgba(0,0,0,.35)}
.hero-copy small{display:block;font-size:15px;margin-bottom:8px}
.hero-copy h1{font-family:"Noto Serif JP",serif;font-size:38px;font-weight:500;letter-spacing:.1em}
/* intro */
.sec-label{background:var(--green);color:#fff;font-size:14px;padding:6px 18px;display:inline-block}
.intro{left:90px;top:868px;width:1020px}
.intro-box{margin-top:8px;border:1px solid var(--line);height:250px;display:flex}
.intro-photo{width:500px;height:100%;background:linear-gradient(120deg,#f5f1ee,#e9dfd9 60%,#d7cfc9)}
.intro-text{flex:1;padding:30px 34px;font-size:13px;line-height:2;color:#666}
.intro-cap{left:140px;top:1070px;background:rgba(255,255,255,.85);padding:6px 20px;font-family:"Noto Serif JP",serif;font-size:22px;color:var(--green-dark)}
.pair{left:90px;top:1180px;width:1020px;display:flex;gap:20px}
.card{flex:1;border:1px solid var(--line);height:230px;padding:14px 22px}
.card h3{text-align:center;font-family:"Noto Serif JP",serif;font-size:20px;color:var(--green-dark);border-bottom:1px solid var(--line);padding-bottom:8px;margin-bottom:14px}
.card p{font-size:12px;line-height:1.9;color:#777}
.doc-photo{width:110px;height:120px;background:linear-gradient(#dfe6ea,#bfcbd2);float:right;margin-left:14px}
.btns{display:flex;gap:14px;margin-top:30px}
.btn{flex:1;height:28px;background:var(--green);color:#fff;font-size:11px;display:flex;align-items:center;justify-content:center}
/* panels */
.panel{top:1470px;width:600px;height:560px;padding:40px 70px 0}
.panel.left{left:0;background:linear-gradient(#fdeef3,#f6e6ec)}
.panel.right{left:600px;background:linear-gradient(#e4f3ef,#dcefee)}
.panel h2{font-family:"Noto Serif JP",serif;font-weight:500;font-size:21px;line-height:1.6;color:var(--pink);margin-bottom:24px}
.panel.right h2{color:var(--green-dark)}
.tiles{display:grid;grid-template-columns:1fr 1fr;gap:14px}
.tile{height:118px;position:relative}
.tile span{position:absolute;left:14px;top:36px;background:rgba(255,255,255,.9);color:var(--pink);font-size:17px;padding:6px 16px;border:1px solid var(--pink);border-radius:3px;white-space:nowrap}
.panel.right .tile span{color:var(--green-dark);border-color:var(--green)}
.t1{background:linear-gradient(#f3e9e3,#e2cfc5)}.t2{background:linear-gradient(#eef0f2,#d6dde2)}
.t3{background:linear-gradient(#f1ece9,#dccfc8)}.t4{background:linear-gradient(#f4eeec,#e3d6d2)}
/* news */
.news{left:90px;top:2050px;width:1020px;display:flex;gap:20px}
.col{flex:1}
.col-head{display:flex;justify-content:space-between;align-items:center;background:var(--green);color:#fff;font-size:13px;padding:5px 14px}
.col-head a{font-size:11px;color:#fff}
.row{display:flex;gap:16px;font-size:12px;border-bottom:1px dotted var(--line);padding:9px 6px;color:#666;white-space:nowrap}
.row b{font-weight:400;color:var(--green-dark);width:80px}
.banners{left:150px;top:2310px;width:900px;display:flex;gap:20px}
.banner{flex:1;height:110px;display:flex;align-items:center;justify-content:flex-end;padding-right:30px;border:1px solid var(--line)}
.banner.blog{background:linear-gradient(90deg,#f2e3e6,#fff 55%)}
.banner.blog strong{font-family:"Montserrat",sans-serif;font-size:30px;letter-spacing:.15em;color:var(--green-dark);font-weight:500}
.banner.staff{background:linear-gradient(90deg,#fff,#dfe9ec)}
.banner.staff .brand{font-size:14px}
/* access */
.access{left:90px;top:2445px;width:1020px}
.access-body{display:flex;gap:30px;margin-top:14px}
.access-text{flex:1;font-size:12px;line-height:2;color:#666}
.access-text h4{font-size:13px;color:var(--text);margin-top:8px}
.map{width:510px;height:300px;background:linear-gradient(135deg,#eceae6,#e0ddd7);position:relative}
.map svg{position:absolute;left:235px;top:120px}
/* footer */
.footer{left:0;top:2828px;width:1200px;height:356px;background:var(--green);color:#fff;padding:26px 90px}
.links{display:grid;grid-template-columns:repeat(6,1fr);gap:4px 20px;font-size:11px}
.links li{list-style:none;white-space:nowrap}
.links li::before{content:"";display:inline-block;width:5px;height:5px;background:#fff;margin-right:6px;vertical-align:middle}
.foot-brand{text-align:center;margin-top:36px}
.foot-brand .brand{color:#fff;justify-content:center;font-size:16px}
.foot-brand .brand .dot{background:#fff}
.foot-brand p{font-size:11px;margin-top:6px}
.foot-tel{font-family:"Montserrat",sans-serif;font-size:30px;margin-top:8px}
.copy{position:absolute;left:0;bottom:0;width:1200px;height:34px;background:var(--green-dark);font-size:10px;display:flex;align-items:center;justify-content:center}
</style>
</head>
<body>

<div class="abs hero" role="img" aria-label="クリニック外観の写真"></div>
<header class="abs header">
  <div class="brand"><span class="dot"></span>SORANE MATERNITY CLINIC</div>
  <nav class="nav"><span>ホーム</span><span>当院の特徴</span><span>診療案内</span><span>出産について</span><span>施設紹介</span><span>採用情報</span><span>アクセス</span></nav>
  <div class="tel"><span class="tel-icon"><svg width="16" height="16" viewBox="0 0 24 24"><path fill="#fff" d="M6.6 10.8a15 15 0 006.6 6.6l2.2-2.2c.3-.3.7-.4 1-.2 1.1.4 2.3.6 3.6.6.6 0 1 .4 1 1V20c0 .6-.4 1-1 1A17 17 0 013 4c0-.6.4-1 1-1h3.5c.6 0 1 .4 1 1 0 1.3.2 2.5.6 3.6.1.3 0 .7-.2 1z"/></svg></span>086-400-2718</div>
</header>
<div class="abs reserve">インターネット予約</div>
<div class="abs hero-copy"><small>女性のための産婦人科</small><h1>はじめての出産でも安心</h1></div>

<section class="abs intro">
  <span class="sec-label">女性に優しい空音産婦人科</span>
  <div class="intro-box">
    <div class="intro-photo" role="img" aria-label="赤ちゃんを抱く母親の写真"></div>
    <div class="intro-text">空音産婦人科は地域の女性の健康を支えるクリニックです。妊娠・出産・婦人科の診療まで、一人ひとりに寄り添った丁寧な医療を心がけております。初めての出産でも安心してお過ごしいただけるよう、経験豊富なスタッフがサポートいたします。お気軽にご相談ください。</div>
  </div>
</section>
<div class="abs intro-cap">安心のお産をサポート</div>

<div class="abs pair">
  <div class="card">
    <h3>院長ご挨拶</h3>
    <div class="doc-photo" role="img" aria-label="院長の写真"></div>
    <p>患者様の不安に寄り添い、安全で快適な出産を目指しております。地域の皆様に信頼される医院として努めてまいります。</p>
    <p style="margin-top:8px">院長　空音 一郎</p>
  </div>
  <div class="card">
    <h3>診療時間・予約</h3>
    <p>診療は予約制です。インターネットまたはお電話にてご予約いただけます。急な症状の際もお気軽にご連絡ください。</p>
    <div class="btns"><span class="btn">外来診療のご案内</span><span class="btn">ネット予約はこちら</span></div>
  </div>
</div>

<section class="abs panel left">
  <h2>女性ならではの不安、お悩みに親身に対応。<br>一人で抱え込む前に、まずはご相談ください。</h2>
  <div class="tiles">
    <div class="tile t1" role="img" aria-label="妊婦健診の写真"><span>妊婦健診</span></div>
    <div class="tile t2" role="img" aria-label="出産の写真"><span>出産</span></div>
    <div class="tile t3" role="img" aria-label="診察の写真"><span>不妊治療</span></div>
    <div class="tile t4" role="img" aria-label="婦人科診療の写真"><span>婦人科</span></div>
    <div class="tile t2" role="img" aria-label="検査の写真"><span>各種検査</span></div>
    <div class="tile t1" role="img" aria-label="予防接種の写真"><span>予防接種</span></div>
  </div>
</section>
<section class="abs panel right">
  <h2>女性を笑顔に導けるよう、<br>コミュニケーションを大切にしています。</h2>
  <div class="tiles">
    <div class="tile t2" role="img" aria-label="病室の写真"><span>入院生活</span></div>
    <div class="tile t3" role="img" aria-label="食事の写真"><span>お食事</span></div>
    <div class="tile t1" role="img" aria-label="妊婦の写真"><span>マタニティ教室</span></div>
    <div class="tile t4" role="img" aria-label="施設の写真"><span>施設紹介</span></div>
    <div class="tile t1" role="img" aria-label="お知らせの写真"><span>お知らせ</span></div>
    <div class="tile t2" role="img" aria-label="スマートフォンの写真"><span>SNS</span></div>
  </div>
</section>

<section class="abs news">
  <div class="col">
    <div class="col-head">お知らせ<a>一覧を見る</a></div>
    <div class="row"><b>2018.7.15</b>7月26日(木)・27日(金)は休診となります。</div>
    <div class="row"><b>2018.7.15</b>7月26日(木)・27日(金)は休診となります。</div>
    <div class="row"><b>2018.7.15</b>7月26日(木)・27日(金)は休診となります。</div>
    <div class="row"><b>2018.7.15</b>7月26日(木)・27日(金)は休診となります。</div>
    <div class="row"><b>2018.7.15</b>7月26日(木)・27日(金)は休診となります。</div>
    <div class="row"><b>2018.7.15</b>7月26日(木)・27日(金)は休診となります。</div>
  </div>
  <div class="col">
    <div class="col-head">今後の予定<a>今後の予定一覧</a></div>
    <div class="row"><b>○月○日</b>マタニティクラス 13:30〜</div>
    <div class="row"><b>○月○日</b>マタニティクラス 13:30〜</div>
    <div class="row"><b>○月○日</b>マタニティクラス 13:30〜</div>
    <div class="row"><b>○月○日</b>マタニティクラス 13:30〜</div>
    <div class="row"><b>○月○日</b>マタニティクラス 13:30〜</div>
    <div class="row"><b>○月○日</b>マタニティクラス 13:30〜</div>
  </div>
</section>

<div class="abs banners">
  <div class="banner blog" role="img" aria-label="妊婦の写真とブログ案内"><strong>BLOG</strong></div>
  <div class="banner staff" role="img" aria-label="スタッフ集合写真"><div class="brand"><span class="dot"></span>SORANE MATERNITY CLINIC</div></div>
</div>

<section class="abs access">
  <span class="sec-label">アクセス</span>
  <div class="access-body">
    <div class="access-text">
      <h4>電車でお越しの方</h4>
      <p>・○○線「○○駅」から徒歩5分<br>・○○線「○○駅」北口より徒歩8分</p>
      <h4>車でお越しの方</h4>
      <p>・○○通りを南へ進み二つ目の信号を右折<br>・当院専用駐車場20台完備<br>・駐車料金は無料です</p>
      <h4>住所</h4>
      <p>〒000-0000　○○県○○市○○町1-2-3</p>
    </div>
    <div class="map" role="img" aria-label="周辺地図">
      <svg width="40" height="52" viewBox="0 0 24 32"><path fill="#e0454a" d="M12 0C5.4 0 0 5.4 0 12c0 9 12 20 12 20s12-11 12-20C24 5.4 18.6 0 12 0z"/><circle cx="12" cy="12" r="4.5" fill="#fff"/></svg>
    </div>
  </div>
</section>

<footer class="abs footer">
  <ul class="links">
    <li>当院の特徴</li><li>外来診療</li><li>出産について</li><li>入院案内</li><li>院長挨拶</li><li>採用情報</li>
    <li>施設紹介</li><li>妊婦健診</li><li>分娩の流れ</li><li>お食事</li><li>スタッフ紹介</li><li>よくある質問</li>
    <li>診療時間</li><li>不妊治療</li><li>無痛分娩</li><li>面会について</li><li>お知らせ</li><li>プライバシー</li>
    <li>アクセス</li><li>婦人科</li><li>産後ケア</li><li>費用について</li><li>ブログ</li><li>サイトマップ</li>
  </ul>
  <div class="foot-brand">
    <div class="brand"><span class="dot"></span>SORANE MATERNITY CLINIC</div>
    <p>空音産婦人科　〒000-0000 ○○県○○市○○町1-2-3</p>
    <div class="foot-tel">086-400-2718</div>
  </div>
  <div class="copy">Copyright © SORANE MATERNITY CLINIC All Rights Reserved.</div>
</footer>

</body>
</html>
```